Sharepoint Banners and Header design

I need some Sharepoint Extended headers and some fixed graphics made for our intranet site.

The intranet is for the school (not the strategic plan) and the words and graphics in the two designs should be complementary as they are on the same page (avoid large amounts of duplication).

I have created a mockup of a new intranet, showing a cropped photo where the header would fit. I have also inserted snippets of some plans where i would like a graphic that highlights our focus areas for the year, our values and our motto 'Strive to Accomplish'.

I would like the graphic to highlight the following (See the image titled example for header):

2021 Explicit Improvement Focus:
- Curriculum
- Consistency
- Knowing our Learners

Our values (Please use the design idea in the example header, where there is one C and the words are listed after it).
- Consideration
- Cooperation
- Courtesy
- Commitment
- Common Sense

2020 - 2023 Strategic Priorities (using the icons from the strategic plan)
- Written and Enacted Curriculum
- Community
- Growth
- Culture of Wellbeing

I have included examples of the type of graphic i am looking for, and an example of a header from the another school.

I have also included some images that might be useful.

I think the SharePoint extended header size is 2560 x 164

The graphic size is 1204 wide and should be landscape.

```html
<!DOCTYPE html>
<html lang="en">
<head>
<meta charset="utf-8">
<title>Intranet Header and Focus Graphic</title>
<link href="https://fonts.googleapis.com/css2?family=Montserrat:wght@500;600;700;800&family=Caveat:wght@500&display=swap" rel="stylesheet">
<style>
  :root {
    --navy: #00007f;
    --royal: #1a22b8;
    --band-top: #3a56e6;
    --band-bottom: #0a0c9c;
    --pill: #3d5cea;
    --value-text: #1616a6;
    --arc-text: #3b4fd8;
    --white: #ffffff;
    --page: #ffffff;
  }
  * { margin: 0; padding: 0; box-sizing: border-box; }
  html, body { width: 1200px; height: 774px; overflow: hidden; background: var(--page); }
  body { position: relative; font-family: "Montserrat", Arial, sans-serif; }

  /* Header strip */
  .site-header {
    position: absolute; left: 58px; top: 140px; width: 1080px; height: 66px;
    background: linear-gradient(180deg, var(--band-top), var(--band-bottom));
    box-shadow: 0 2px 4px rgba(0,0,0,.35);
    overflow: hidden;
  }
  .header-photo { position: absolute; top: 0; height: 66px; }
  .header-photo--left { left: 0; width: 118px; background: linear-gradient(90deg, #4d6b45, #6b7e62 55%, rgba(58,86,230,0)); }
  .header-photo--right { right: 0; width: 190px; background: linear-gradient(90deg, rgba(58,86,230,0), #7d8a5a 25%, #a6b2c4 55%, #2c3a5a); }
  .header-school {
    position: absolute; left: 318px; top: 17px; width: 110px;
    color: var(--white); font-weight: 600; font-size: 11px; line-height: 1.2; text-align: center;
  }
  .header-motto {
    position: absolute; left: 460px; top: -4px;
    font-family: "Caveat", cursive; font-weight: 500; font-size: 60px; color: var(--white);
    letter-spacing: 1px; white-space: nowrap;
  }

  /* Focus graphic */
  .focus-card {
    position: absolute; left: 187px; top: 266px; width: 824px; height: 388px;
    background: var(--white); box-shadow: 0 1px 5px rgba(0,0,0,.35); overflow: hidden;
  }
  .focus-title {
    position: absolute; left: 0; top: 27px; width: 300px; height: 60px;
    background: linear-gradient(180deg, var(--band-top), var(--band-bottom));
    border-radius: 0 30px 30px 0; color: var(--white);
  }
  .focus-year { position: absolute; left: 0; width: 272px; top: -2px; text-align: center; font-weight: 700; font-size: 36px; line-height: 40px; }
  .focus-label { position: absolute; left: 11px; top: 34px; font-weight: 500; font-size: 18px; white-space: nowrap; }
  .focus-item {
    position: absolute; left: 0; height: 22px; padding-left: 36px;
    background: var(--pill); border-radius: 0 11px 11px 0; color: var(--white);
    font-weight: 500; font-size: 15px; line-height: 22px;
  }
  .focus-item::before {
    content: ""; position: absolute; left: 21px; top: 7px; width: 8px; height: 8px; border-radius: 50%; background: var(--white);
  }
  .value-word {
    position: absolute; left: 486px; font-weight: 700; font-size: 18.5px; color: var(--value-text);
    line-height: 20px; white-space: nowrap;
  }

  .priorities {
    position: absolute; left: 0; top: 219px; width: 824px; height: 169px;
    background: linear-gradient(180deg, #2c40d4, var(--band-bottom));
  }
  .priorities-band {
    position: absolute; left: 0; top: 0; width: 824px; height: 49px;
    background: linear-gradient(180deg, var(--band-top), var(--band-bottom));
  }
  .priorities-title {
    position: absolute; left: 191px; top: 0; color: var(--white); font-weight: 700; font-size: 40px; line-height: 48px; white-space: nowrap;
    text-shadow: 0 2px 3px rgba(0,0,0,.35);
  }
  .priorities-title small { font-size: 27px; }
  .school-name {
    position: absolute; left: 30px; top: 80px; width: 130px; color: var(--white);
    font-weight: 700; font-size: 15px; line-height: 1.3; text-align: center;
  }
  .priority {
    position: absolute; height: 26px; padding-left: 32px;
    background: var(--pill); border-radius: 0 13px 13px 0; color: var(--white);
    font-weight: 500; font-size: 17.5px; line-height: 26px; white-space: nowrap;
  }
  .priority-icon {
    position: absolute; width: 50px; height: 50px; border-radius: 50%;
    background: radial-gradient(circle at 50% 40%, #2a3ad0, #08108a); border: 1.5px solid #4b64f0;
  }
  .overlay { position: absolute; left: 0; top: 0; }
</style>
</head>
<body>

<header class="site-header">
  <div class="header-photo header-photo--left" role="img" aria-label="Photo of a smiling student"></div>
  <div class="header-school">Kestrel Vale<br>High School</div>
  <div class="header-motto">Strive to Accomplish</div>
  <div class="header-photo header-photo--right" role="img" aria-label="Photo of two students outdoors"></div>
</header>

<section class="focus-card">
  <div class="focus-title">
    <div class="focus-year">2021</div>
    <div class="focus-label">Explicit Improvement Focus</div>
  </div>
  <div class="focus-item" style="top:99px;width:212px;">Knowing our Learners</div>
  <div class="focus-item" style="top:133px;width:147px;">Consistency</div>
  <div class="focus-item" style="top:167px;width:135px;">Curriculum</div>

  <div class="value-word" style="top:47px;">OMMON SENSE</div>
  <div class="value-word" style="top:79px;">OMMITMENT</div>
  <div class="value-word" style="top:111px;">OURTESY</div>
  <div class="value-word" style="top:142px;">OOPERATION</div>
  <div class="value-word" style="top:172px;">ONSIDERATION</div>

  <div class="priorities">
    <div class="priorities-band"></div>
    <div class="priorities-title">Strategic Priorities <small>(2020 - 2023)</small></div>
    <div class="school-name">Kestrel Vale High School</div>

    <div class="priority" style="left:228px;top:63px;width:295px;">Written &amp; Enacted Curriculum</div>
    <div class="priority" style="left:228px;top:115px;width:216px;">Culture of Wellbeing</div>
    <div class="priority" style="left:588px;top:63px;width:149px;">Community</div>
    <div class="priority" style="left:588px;top:115px;width:111px;">Growth</div>
    <div class="priority-icon" style="left:204px;top:50px;"></div>
    <div class="priority-icon" style="left:204px;top:102px;"></div>
    <div class="priority-icon" style="left:564px;top:50px;"></div>
    <div class="priority-icon" style="left:564px;top:102px;"></div>
    <svg class="overlay" width="824" height="169" viewBox="0 0 824 169" fill="none" stroke="#fff" stroke-width="1.6" stroke-linecap="round" stroke-linejoin="round" aria-hidden="true">
      <rect x="219" y="64" width="18" height="22" rx="2"/><path d="M223 70h10M223 75h10M223 80h7"/>
      <circle cx="229" cy="121" r="4"/><path d="M220 136c2-6 5-9 9-9s7 3 9 9M217 124v8M241 124v8"/>
      <circle cx="583" cy="71" r="3.5"/><circle cx="592" cy="71" r="3.5"/><circle cx="601" cy="71" r="3.5"/><path d="M577 85c1-5 4-7 6-7s5 2 6 7M595 85c1-5 4-7 6-7s5 2 6 7"/>
      <path d="M578 136l8-8 5 5 10-12M596 121h5v5"/>
    </svg>
  </div>

  <svg class="overlay" width="824" height="388" viewBox="0 0 824 388" aria-hidden="true">
    <defs>
      <path id="values-arc" d="M352 176 A100 100 0 0 1 476 28"/>
    </defs>
    <path d="M479.3 76 A67 67 0 1 0 479.3 162" fill="none" stroke="var(--navy)" stroke-width="27"/>
    <text font-family="Montserrat, Arial, sans-serif" font-weight="700" font-size="21" fill="var(--arc-text)" letter-spacing="1">
      <textPath href="#values-arc">OUR VALUES</textPath>
    </text>
    <g stroke="var(--navy)" stroke-width="2" fill="var(--navy)">
      <line x1="642" y1="57" x2="720" y2="57"/><circle cx="642" cy="57" r="3"/>
      <line x1="620" y1="89" x2="676" y2="89"/><circle cx="620" cy="89" r="3"/>
      <line x1="587" y1="121" x2="720" y2="121"/><circle cx="587" cy="121" r="3"/>
      <line x1="627" y1="152" x2="676" y2="152"/><circle cx="627" cy="152" r="3"/>
      <line x1="647" y1="182" x2="720" y2="182"/><circle cx="647" cy="182" r="3"/>
    </g>
    <g fill="var(--royal)" stroke="var(--navy)" stroke-width="2">
      <circle cx="767" cy="60" r="23"/>
      <circle cx="700" cy="91" r="23"/>
      <circle cx="767" cy="121" r="23"/>
      <circle cx="700" cy="151" r="23"/>
      <circle cx="767" cy="181" r="23"/>
    </g>
    <g fill="none" stroke="#fff" stroke-width="1.5" stroke-linecap="round" stroke-linejoin="round">
      <circle cx="767" cy="55" r="6"/><path d="M764 62v5h6v-5"/>
      <circle cx="700" cy="85" r="6"/><path d="M690 101c1-6 5-9 10-9s9 3 10 9"/>
      <circle cx="760" cy="117" r="3"/><circle cx="767" cy="115" r="3"/><circle cx="774" cy="117" r="3"/><path d="M756 128l8-3h12"/>
      <rect x="691" y="142" width="18" height="13" rx="1"/><path d="M693 160h14"/>
      <circle cx="767" cy="181" r="8"/><circle cx="767" cy="181" r="3"/>
    </g>
  </svg>
</section>

</body>
</html>
```